Website for a web design agency

We are a website and marketing agency. We do website design, development, and well as Brindle and Quorvia advertising and analytics. We ourselves need a new website for our own brand. We are working on some designs in-house with our own designers, but we also wanted to see what outside designers would come up with.
We are starting off with the homepage, and here is the breakdown of the sections:
https://files.brindlework.example/sheet/d/7kqTr2VnPLwXeHsaMcY4oBfJzuGNtKdWiEh3Rx9pLmQb/view?mode=share
This doc also has many links to sites we have done, which you can take screenshots of for the portfolio section.
In terms of the "look" I am going for, I want to look high-end and very beautiful designs. I found this website that I like a lot that you can use some of the elements of, just as a starting point:
http://velmarkstudio.example/layouts/pixelbarn/html/ostrevo/index.html and here is another design option they have http://velmarkstudio.example/layouts/pixelbarn/html/ostrevo/index-4.html
I'm also uploading my logo. The logo matches the gold and black look from these websites, but I would be open to switching to another color scheme if needed.
This is the link to my very old website, which you can use for some of the dummy text, and a pic of myself. I will be taking more pics of myself:
https://theplumtreeandwillowgroup.example/
We need a homepage and a portfolio page right now, but if you are the winner, we will be hiring you to make additional pages.
Updates
More designs continue to come in even today, and I want to make sure no other designers are still submitting designs.
Target Market(s)
medium and large businesses owners, and non-profits
Number of Pages Required
1 page

```html
<!DOCTYPE html>
<html lang="en">
<head>
<meta charset="utf-8">
<title>Kestran — Web Design &amp; Marketing Agency</title>
<link rel="stylesheet" href="https://fonts.googleapis.com/css2?family=Montserrat:wght@300;400;500;600;700;800;900&family=Comfortaa:wght@400;600&display=swap">
<style>
:root{
  --gold:#f6b21b;
  --gold-soft:#f8c54e;
  --gold-deep:#eea412;
  --ink:#121212;
  --ink-soft:#2a2a2a;
  --brown:#4a3410;
  --cream:#f4efe8;
  --card-cream:#fdf1d8;
  --muted:#777;
  --white:#fff;
  --line:#d9d9d9;
}
*{box-sizing:border-box;margin:0;padding:0}
html,body{width:1200px;height:4930px;overflow:hidden}
body{font-family:'Montserrat',sans-serif;color:var(--ink);background:var(--white)}
.page{position:relative;width:1200px;height:4930px;overflow:hidden}
section,header,footer{position:absolute;left:0;width:1200px;overflow:hidden}
.abs{position:absolute}
.ghost{position:absolute;font-weight:900;letter-spacing:2px;line-height:1;white-space:nowrap}
.eyebrow{position:absolute;font-size:11px;color:var(--ink-soft);display:flex;align-items:center;gap:14px}
.eyebrow::before{content:"";display:block;width:136px;height:2px;background:var(--gold)}
.eyebrow.right{justify-content:flex-end}
.h2{position:absolute;font-weight:900;font-size:27px;letter-spacing:.3px;text-transform:uppercase;line-height:1.6}

/* brand name placeholder */
.brand{display:flex;align-items:center;gap:7px}
.brand-mark{width:9px;height:9px;background:var(--gold)}
.brand-name{font-family:'Montserrat',sans-serif;font-weight:700;font-size:15px;letter-spacing:1px;color:var(--gold)}

/* header / hero */
.hero{top:0;height:605px;background:linear-gradient(100deg,#050505 0%,#0d0b08 45%,#2e220c 75%,#6a4b12 100%)}
.logo-box{position:absolute;left:201px;top:0;width:149px;height:92px;background:#000;display:flex;align-items:center;justify-content:center}
.nav{position:absolute;top:25px;left:459px;display:flex;gap:36px;font-size:10px;font-weight:500;color:#ddd}
.nav a{color:inherit;text-decoration:none}
.nav a.active{border-bottom:1px solid var(--gold);padding-bottom:4px}
.search{position:absolute;left:915px;top:15px;width:33px;height:33px;background:var(--gold);display:flex;align-items:center;justify-content:center}
.hero .ghost{font-size:78px;color:#1e1e1e;top:94px}
.hero-kicker{position:absolute;left:212px;top:170px;font-size:10px;font-weight:600;color:#fff;letter-spacing:.5px}
.hero-title{position:absolute;left:210px;top:188px;font-size:74px;font-weight:900;color:#fff;line-height:1.1;letter-spacing:1px}
.hero-title .outline{color:transparent;-webkit-text-stroke:2px var(--gold)}
.hero-sub{position:absolute;left:212px;top:371px;font-size:11.5px;color:#eee}
.btn-outline{position:absolute;display:flex;align-items:center;justify-content:center;font-size:10px;font-weight:700;letter-spacing:.5px;text-transform:uppercase}
.hero .btn-outline{left:212px;top:413px;width:165px;height:46px;border:2px solid #fff;color:#fff}
.video{position:absolute;left:645px;top:168px;width:517px;height:288px;background:linear-gradient(135deg,#b9b6b0 0%,#8d8a85 60%,#6f6c67 100%)}
.video-play{position:absolute;left:214px;top:128px;width:32px;height:32px;border-radius:50%;background:var(--gold);display:flex;align-items:center;justify-content:center}
.video-name{position:absolute;left:0;top:190px;font-family:'Comfortaa',sans-serif;font-size:26px;color:#fff;line-height:1.15;text-align:center;width:270px}
.fullscreen{position:absolute;left:1009px;top:434px;width:107px;height:44px;background:#fff;font-size:10px;font-weight:600;display:flex;align-items:center;justify-content:center}
.fullscreen-btn{position:absolute;left:1116px;top:434px;width:46px;height:44px;background:var(--gold);display:flex;align-items:center;justify-content:center}

/* services */
.services{top:605px;height:685px;background:linear-gradient(180deg,#f4b023 0%,#f6b51f 60%,#f3ac19 100%)}
.services .ghost{color:rgba(255,255,255,.18)}
.svc{position:absolute;width:230px;background:rgba(255,214,110,.55);padding:34px 32px 0;color:var(--ink)}
.svc.dark{background:#2a1e0b;color:#fff}
.svc-num{font-size:13px;font-weight:800;display:flex;align-items:center;gap:8px}
.svc-num::after{content:"";width:30px;height:2px;background:currentColor}
.svc h3{font-size:16px;font-weight:800;margin-top:22px;line-height:1.5}
.svc p{font-size:11px;line-height:1.75;margin-top:12px}
.more{display:flex;align-items:center;gap:12px;font-size:10px;font-weight:800;margin-top:18px;text-transform:uppercase}
.more .plus{width:16px;height:16px;background:#fff;display:flex;align-items:center;justify-content:center;font-size:12px;color:var(--ink);font-weight:700}

/* insight */
.insight{top:1290px;height:547px;background:#fff}
.insight .ghost{left:0;top:46px;font-size:80px;color:#ebebeb}
.insight-photo-bg{position:absolute;left:178px;top:160px;width:410px;height:303px;background:var(--gold);border-radius:150px 0 0 0}
.insight-photo{position:absolute;left:300px;top:50px;width:288px;height:413px;background:linear-gradient(180deg,#d8d2cb 0%,#eae6e1 60%,#c6c0b9 100%)}
.insight .eyebrow{left:733px;top:130px}
.insight .h2{left:681px;top:148px;line-height:1.7}
.insight p{position:absolute;left:681px;width:300px;font-size:11px;line-height:1.75;color:#333}
.insight .btn-outline{left:681px;top:415px;width:167px;height:46px;border:2px solid var(--ink);color:var(--ink)}

/* portfolio */
.portfolio{top:1837px;height:590px;background:#fff}
.portfolio .eyebrow{left:226px;top:30px}
.portfolio .h2{left:224px;top:52px}
.portfolio .ghost{left:731px;top:44px;font-size:56px;color:#ececec}
.shot{position:absolute}
.dots{position:absolute;display:flex;gap:5px;align-items:center}
.dots i{display:block;width:4px;height:4px;border-radius:50%;background:var(--ink)}
.dots i.on{width:14px;height:3px;border-radius:2px}

/* case studies */
.cases{top:2427px;height:390px;background:var(--cream)}
.cases-circle{position:absolute;left:226px;top:60px;width:300px;height:300px;border-radius:50%;background:#f2e5c9}
.cases .eyebrow{right:226px;top:30px}
.cases .h2{right:226px;top:58px}
.case{position:absolute;top:126px;height:188px;color:#fff}
.case-cap{position:absolute;left:18px;bottom:14px;font-size:10px;line-height:1.5}
.case-cap b{display:block;font-size:11px;margin-bottom:3px}
.case.dark{background:#2b2b2b;left:609px;width:312px}
.case.dark .case-text{position:absolute;left:37px;top:20px;width:238px;font-size:10px;line-height:1.75}
.case.dark .case-text b{display:block;text-align:center;font-size:11px;margin-bottom:18px}

/* stats */
.stats{top:2817px;height:155px;background:var(--gold)}
.stat{position:absolute;top:55px;display:flex;align-items:center;gap:18px}
.stat-num{font-size:40px;font-weight:900;color:#fff;letter-spacing:1px}
.stat-label{font-size:10px;font-weight:600;line-height:1.6;color:var(--ink)}

/* help */
.help{top:2972px;height:517px;background:#fff}
.help .eyebrow{left:475px;top:66px}
.help .h2{left:0;width:1200px;text-align:center;top:92px}
.help-card{position:absolute;top:173px;width:230px;height:250px;background:var(--card-cream);padding:42px 32px 0}
.help-card h3{font-size:15px;font-weight:800}
.help-card .big{position:absolute;right:4px;top:10px;font-size:64px;font-weight:900;color:transparent;-webkit-text-stroke:2px #fff;line-height:1}
.help-card p{font-size:11px;line-height:1.75;margin-top:22px;color:#333}
.help-card .more{color:var(--gold);margin-top:14px}
.help-card .more .plus{border:1px solid var(--gold);color:var(--gold)}

/* testimonials */
.testimonials{top:3489px;height:391px;background:var(--cream)}
.testimonials .eyebrow{left:462px;top:32px}
.testimonials .h2{left:224px;top:58px}
.testimonials .ghost{left:783px;top:26px;font-size:54px;color:#e6dfd6}
.quote-mark{position:absolute;left:226px;top:180px;font-size:44px;font-style:italic;font-weight:300;color:var(--gold)}
.quote{position:absolute;left:281px;top:177px;width:330px;font-size:11.5px;line-height:1.7;color:#333}
.author-avatar{position:absolute;left:281px;top:293px;width:36px;height:36px;border-radius:50%;background:#9e9e9e}
.author-name{position:absolute;left:332px;top:295px;font-size:13px;font-weight:700}
.author-role{position:absolute;left:332px;top:316px;font-size:10px;color:var(--muted)}
.thumbs{position:absolute;left:0;top:0;isolation:isolate}
.thumb{position:absolute;width:60px;height:60px}
.thumb.framed::after{content:"";position:absolute;right:-6px;bottom:-6px;width:60px;height:60px;border:3px solid var(--gold);z-index:-1}

/* team */
.team{top:3880px;height:580px;background:#fff}
.team .ghost{left:18px;top:98px;font-size:112px;color:#ededed}
.team .eyebrow{right:226px;top:70px}
.team .h2{right:226px;top:94px}
.member{position:absolute;top:172px;width:230px;text-align:center}
.member-photo{width:230px;height:251px;position:relative}
.socials{position:absolute;left:50%;transform:translateX(-50%);bottom:18px;display:flex;background:var(--gold)}
.socials span{width:22px;height:22px;display:flex;align-items:center;justify-content:center}
.socials span i{display:block;width:8px;height:8px;border-radius:50%;border:1.5px solid #fff}
.member h4{font-size:15px;font-weight:600;margin-top:24px;text-transform:uppercase}
.member small{display:block;font-size:10px;color:var(--muted);margin-top:8px}

/* contact + footer */
.foot-band{top:4689px;height:241px;background:linear-gradient(100deg,#050505 0%,#0f0c08 55%,#3a2a0c 85%,#6a4b12 100%)}
.contact{top:4456px;left:224px;width:750px;height:407px;overflow:visible}
.contact-form{position:absolute;left:0;top:0;width:549px;height:407px;background:#fff;padding:0 32px}
.contact-form h2{position:absolute;left:32px;top:25px;font-size:21px;font-weight:800}
.contact-form .sub{position:absolute;left:32px;top:67px;font-size:10.5px;color:#555}
.field{position:absolute;border:1px solid #cfcfcf;font-size:10px;color:#888;padding:0 18px;display:flex;align-items:center}
.field.area{align-items:flex-start;padding-top:14px}
.submit{position:absolute;left:32px;top:338px;width:125px;height:37px;background:var(--gold);color:#fff;font-size:10px;font-weight:700;display:flex;align-items:center;justify-content:center}
.contact-info{position:absolute;left:549px;top:0;width:201px;height:407px;background:var(--gold);padding:0 24px}
.contact-info h5{position:absolute;left:31px;top:28px;font-size:10.5px;font-weight:600}
.ci-line{position:absolute;left:31px;width:140px;height:1px;background:rgba(0,0,0,.35)}
.ci-row{position:absolute;left:31px;display:flex;gap:16px;font-size:10px;line-height:1.75;color:var(--ink)}
.ci-row svg{flex:none;margin-top:2px}
.ci-brand{position:absolute;left:0;width:201px;top:346px;justify-content:center}
.ci-brand .brand-mark{background:#fff}
.ci-brand .brand-name{color:#fff}
.copyright{position:absolute;left:224px;top:203px;font-size:10px;color:#ddd}
.foot-social{position:absolute;top:193px;display:flex;gap:14px;left:866px}
.foot-social span{width:28px;height:28px;border-radius:50%;border:1px solid #ddd;display:flex;align-items:center;justify-content:center}
.foot-social span i{display:block;width:8px;height:8px;border-radius:50%;background:#ddd}
</style>
</head>
<body>
<div class="page">

<header class="hero">
  <div class="logo-box"><div class="brand"><span class="brand-mark"></span><span class="brand-name">KESTRAN</span></div></div>
  <nav class="nav"><a class="active" href="#">HOME</a><a href="#">ABOUT</a><a href="#">PORTFOLIO</a><a href="#">CONTACT</a></nav>
  <div class="search"><svg width="14" height="14" viewBox="0 0 14 14" fill="none" stroke="#fff" stroke-width="1.6"><circle cx="6" cy="6" r="4.5"/><path d="M9.5 9.5 13 13"/></svg></div>
  <div class="ghost" style="left:-4px">CODE</div>
  <div class="ghost" style="left:846px">DESIGN</div>
  <div class="hero-kicker">MAKING BRANDS</div>
  <h1 class="hero-title">WE BUILD<br><span class="outline">VALUE</span></h1>
  <p class="hero-sub">Enterprise Level Website Development and Online Marketing</p>
  <a class="btn-outline">See how we do it</a>
  <div class="video" role="img" aria-label="Video still of the agency founder in front of a grey wall">
    <div class="video-play"><svg width="10" height="12" viewBox="0 0 10 12"><path d="M1 1l8 5-8 5z" fill="#fff"/></svg></div>
    <div class="video-name">Dorian Kestran<br>web developer</div>
  </div>
  <div class="fullscreen">Full Screen</div>
  <div class="fullscreen-btn"><svg width="26" height="26" viewBox="0 0 26 26"><circle cx="13" cy="13" r="12" fill="#fff"/><path d="M11 8.5l6 4.5-6 4.5z" fill="#f6b21b"/></svg></div>
</header>

<section class="services">
  <div class="ghost" style="left:0;top:16px;font-size:74px">WHAT WE DO</div>
  <div class="ghost" style="left:985px;top:515px;font-size:52px;line-height:1.2">THINGS<br>WE<br>CRUSH</div>
  <article class="svc" style="left:224px;top:73px;height:254px"><div class="svc-num">01</div><h3>Websites</h3><p>Lorem ipsum dolor sit amet, consetetur sadipscing elitr, sed diam nonumy eirmod tempor invidunt ut labore et</p><div class="more">Know more <span class="plus">+</span></div></article>
  <article class="svc dark" style="left:484px;top:73px;height:254px"><div class="svc-num">02</div><h3>Landing Pages</h3><p>Lorem ipsum dolor sit amet, consetetur sadipscing elitr, sed diam nonumy eirmod tempor invidunt ut labore et</p><div class="more">Know more <span class="plus">+</span></div></article>
  <article class="svc" style="left:745px;top:73px;height:254px"><div class="svc-num">03</div><h3>Donation Pages</h3><p>Lorem ipsum dolor sit amet, consetetur sadipscing elitr, sed diam nonumy eirmod tempor invidunt ut labore et</p><div class="more">Know more <span class="plus">+</span></div></article>
  <article class="svc" style="left:224px;top:358px;height:252px"><div class="svc-num">04</div><h3>PPC &amp; Funnels</h3><p>Lorem ipsum dolor sit amet, consetetur sadipscing elitr, sed diam nonumy eirmod tempor invidunt ut labore et</p><div class="more">Know more <span class="plus">+</span></div></article>
  <article class="svc" style="left:484px;top:358px;height:252px"><div class="svc-num">05</div><h3>Video Marketing</h3><p>Lorem ipsum dolor sit amet, consetetur sadipscing elitr, sed diam nonumy eirmod tempor invidunt ut labore et</p><div class="more">Know more <span class="plus">+</span></div></article>
  <article class="svc" style="left:745px;top:358px;height:252px"><div class="svc-num">06</div><h3>Analytics &amp;<br>Optimisation</h3><p>Lorem ipsum dolor sit amet, consetetur sadipscing elitr, sed diam nonumy eirmod tempor invidunt ut labore et</p><div class="more">Know more <span class="plus">+</span></div></article>
</section>

<section class="insight">
  <div class="ghost">INSIGHT</div>
  <div class="insight-photo-bg"></div>
  <div class="insight-photo" role="img" aria-label="Portrait of the founder in a white shirt"></div>
  <div class="eyebrow">Designing Growth</div>
  <h2 class="h2">What do you need<br>&amp; how we doing it</h2>
  <p style="top:266px">Lorem ipsum dolor sit amet, consetetur sadipscing elitr, sed diam nonumy eirmod tempor invidunt ut labore et dolore magna aliquyam erat,</p>
  <p style="top:332px">Sed diam voluptua. At vero eos et accusam et justo duo dolores et ea rebum. Stet clita kasd gubergren, no sea takimata sanctus est.</p>
  <a class="btn-outline">Learn more</a>
</section>

<section class="portfolio">
  <div class="eyebrow">10+ years Experience</div>
  <h2 class="h2">Recent Projects</h2>
  <div class="ghost">OUR PORTFOLIO</div>
  <div class="shot" style="left:0;top:169px;width:220px;height:277px;background:linear-gradient(180deg,#2c3448 0%,#8a5a3a 30%,#f4f4f4 32%,#eee 100%)" role="img" aria-label="Screenshot of an industrial client website"></div>
  <div class="shot" style="left:220px;top:169px;width:224px;height:277px;background:linear-gradient(180deg,#1d3a7a 0%,#3d5fa8 30%,#fafafa 32%,#f2f2f2 75%,#5b6f8c 100%)" role="img" aria-label="Screenshot of a nonprofit client website"></div>
  <div class="shot" style="left:444px;top:137px;width:308px;height:342px;background:linear-gradient(180deg,#fff 0%,#fff 8%,#16305e 8%,#2a5a9a 35%,#fafafa 35%,#fafafa 58%,#203a66 58%,#4a3a5a 80%,#fff 80%);box-shadow:0 6px 24px rgba(0,0,0,.25)" role="img" aria-label="Screenshot of a film production client website"></div>
  <div class="shot" style="left:783px;top:169px;width:168px;height:277px;background:linear-gradient(180deg,#e9e4dc 0%,#b8a894 50%,#dcd3c6 100%)" role="img" aria-label="Screenshot of an interior design client website"></div>
  <div class="shot" style="left:978px;top:169px;width:222px;height:277px;background:linear-gradient(180deg,#5a6a78 0%,#8b9aa6 40%,#f7f7f7 42%,#eef1f3 100%)" role="img" aria-label="Screenshot of a health and wellness client website"></div>
  <div class="dots" style="left:573px;top:524px"><i></i><i></i><i class="on"></i><i></i><i></i></div>
</section>

<section class="cases">
  <div class="cases-circle"></div>
  <div class="eyebrow right">Growing Businesses</div>
  <h2 class="h2">Latest Case Studies</h2>
  <div class="case" style="left:0;width:258px;background:linear-gradient(135deg,#6a7a86,#9aa6ae)" role="img" aria-label="Diagram of connected business icons">
    <div class="case-cap">ipsum dolor sit amet, consectetur adipiscing elit.<br>urna, maximus eu consequat</div>
  </div>
  <div class="case" style="left:278px;width:312px;background:linear-gradient(135deg,#8a6a4a,#4a5a72)" role="img" aria-label="Team meeting in a modern office">
    <div class="case-cap"><b>Case Study Heading</b>Lorem ipsum dolor sit amet, consectetur adipiscing elit.<br>In purus urna, maximus eu consequat</div>
  </div>
  <div class="case dark">
    <div class="case-text"><b>Case Study Heading</b>Lorem ipsum dolor sit amet, consectetur adipiscing elit. In purus urna, maximus eu consequat non, sollicitudin nec nisi. Cras non urna quis metus gravida vestibulum sit amet id felis. Aliquam nec libero at mauris dictum efficitur.</div>
  </div>
  <div class="case" style="left:940px;width:260px;background:linear-gradient(135deg,#b0a090,#6a5a4e)" role="img" aria-label="Designer working at a laptop">
    <div class="case-cap"><b>Case Study Heading</b>Lorem ipsum dolor sit amet, consectetur adipiscing<br>In purus urna, maximus eu consequat</div>
  </div>
  <div class="dots" style="left:573px;top:356px"><i></i><i></i><i class="on"></i><i></i><i></i></div>
</section>

<section class="stats">
  <div class="stat" style="left:224px"><span class="stat-num">510</span><span class="stat-label">HAPPY<br>CLIENTS</span></div>
  <div class="stat" style="left:507px"><span class="stat-num">350</span><span class="stat-label">PROJECTS<br>COMPLETED</span></div>
  <div class="stat" style="left:819px"><span class="stat-num">106</span><span class="stat-label">PARTNERS<br>WORLDWIDE</span></div>
</section>

<section class="help">
  <div class="eyebrow" style="gap:12px">We Work for you</div>
  <h2 class="h2">How We Help</h2>
  <article class="help-card" style="left:224px"><span class="big">01</span><h3>CREATE</h3><p>I can help you figure out what makes you unique. It's your unique selling point that helps you stand out from the other millions of sites out there.</p><div class="more">Know more <span class="plus">+</span></div></article>
  <article class="help-card" style="left:484px"><span class="big">02</span><h3>BUILD</h3><p>Your website is your own special place online for what you are trying to bring to the world. I help make it stand out and reflect everything you stand for.</p><div class="more">Know more <span class="plus">+</span></div></article>
  <article class="help-card" style="left:745px"><span class="big">03</span><h3>MARKET</h3><p>Between SEO, SEM, social, blogging, &amp; email, web marketing can become overwhelming. I help you figure out the right path for you &amp; your growth.</p><div class="more">Know more <span class="plus">+</span></div></article>
</section>

<section class="testimonials">
  <div class="ghost">TESTIMONIALS</div>
  <div class="eyebrow">Feedback</div>
  <h2 class="h2">What Clients Say About Us</h2>
  <div class="quote-mark">//</div>
  <p class="quote">"They are just awesome people. They are very creative and understand your needs. Dorian is very friendly and is full of very innovative ideas. Me and my team is very happy with the final result plus they are available for you 24/7. Thank you Dorian and his team.</p>
  <div class="author-avatar" role="img" aria-label="Client portrait"></div>
  <div class="author-name">Owen Marlow</div>
  <div class="author-role">CEO at Fernvale</div>
  <svg class="abs" style="left:578px;top:285px" width="32" height="14" viewBox="0 0 32 14" fill="none" stroke-width="2"><path d="M8 2 3 7l5 5" stroke="#ddd"/><path d="M24 2l5 5-5 5" stroke="#f6b21b"/></svg>
  <div class="dots" style="left:562px;top:311px"><i></i><i></i><i class="on"></i><i></i><i></i></div>
  <div class="thumbs">
    <div class="thumb framed" style="left:743px;top:166px;background:#9a8a7a" role="img" aria-label="Client portrait"></div>
    <div class="thumb" style="left:827px;top:140px;background:#6a6a6a" role="img" aria-label="Client portrait"></div>
    <div class="thumb framed" style="left:910px;top:117px;background:#a89a88" role="img" aria-label="Client portrait"></div>
    <div class="thumb" style="left:910px;top:206px;background:#b4aca4" role="img" aria-label="Client portrait"></div>
    <div class="thumb" style="left:827px;top:226px;background:#5e5e5e" role="img" aria-label="Client portrait"></div>
    <div class="thumb framed" style="left:743px;top:258px;background:#3e3a36" role="img" aria-label="Client portrait"></div>
    <div class="thumb" style="left:827px;top:308px;background:#c4bcb4" role="img" aria-label="Client portrait"></div>
    <div class="thumb framed" style="left:910px;top:285px;background:#7a6e66" role="img" aria-label="Client portrait"></div>
  </div>
</section>

<section class="team">
  <div class="ghost">TEAM</div>
  <div class="eyebrow right">10+ Years Experience</div>
  <h2 class="h2">Experts for You</h2>
  <div class="member" style="left:224px"><div class="member-photo" style="background:linear-gradient(180deg,#8a9aa6,#2a3442)" role="img" aria-label="Team member portrait in a navy suit"><div class="socials"><span><i></i></span><span><i></i></span><span><i></i></span><span><i></i></span></div></div><h4>Reed Calloway</h4><small>UI/UX</small></div>
  <div class="member" style="left:484px"><div class="member-photo" style="background:linear-gradient(180deg,#b8c4cc,#8a9aa8)" role="img" aria-label="Team member portrait in a light blazer"><div class="socials"><span><i></i></span><span><i></i></span><span><i></i></span><span><i></i></span></div></div><h4>Milo Hartwell</h4><small>Senior Developer</small></div>
  <div class="member" style="left:745px"><div class="member-photo" style="background:linear-gradient(180deg,#6a4a34,#2a2224)" role="img" aria-label="Team member portrait in a dark suit"><div class="socials"><span><i></i></span><span><i></i></span><span><i></i></span><span><i></i></span></div></div><h4>Ezra Lindqvist</h4><small>Manager</small></div>
</section>

<footer class="foot-band">
  <div class="copyright">©2021 KESTRAN | All Rights Reserved</div>
  <div class="foot-social"><span><i></i></span><span><i></i></span><span><i></i></span></div>
</footer>

<section class="contact">
  <div class="contact-form">
    <h2>GET FREE AUDIT &amp; CONSULTATION</h2>
    <p class="sub">Get in touch with us and get started.</p>
    <div class="field" style="left:32px;top:107px;width:232px;height:37px">Full Name*</div>
    <div class="field" style="left:283px;top:107px;width:234px;height:37px">Phone Number*</div>
    <div class="field" style="left:32px;top:164px;width:232px;height:37px">Email Address*</div>
    <div class="field" style="left:283px;top:164px;width:234px;height:37px">Website Name</div>
    <div class="field area" style="left:32px;top:220px;width:485px;height:97px">Message</div>
    <div class="submit">SUBMIT</div>
  </div>
  <div class="contact-info">
    <h5>Contact Information</h5>
    <div class="ci-line" style="top:95px"></div>
    <div class="ci-row" style="top:132px"><svg width="10" height="13" viewBox="0 0 10 13"><path d="M5 0a5 5 0 0 0-5 5c0 3.5 5 8 5 8s5-4.5 5-8a5 5 0 0 0-5-5zm0 7a2 2 0 1 1 0-4 2 2 0 0 1 0 4z" fill="#111"/></svg><span>123 Your Address,<br>New Street, U.S</span></div>
    <div class="ci-row" style="top:188px"><svg width="11" height="11" viewBox="0 0 11 11"><path d="M2.3 0 0 1.5C0 6.5 4.5 11 9.5 11L11 8.7 8.3 7 7 8.2C5.3 7.5 3.5 5.7 2.8 4L4 2.7z" fill="#111"/></svg><span>765-555-0148</span></div>
    <div class="ci-row" style="top:234px"><svg width="12" height="9" viewBox="0 0 12 9"><rect width="12" height="9" fill="#111"/><path d="M0 0l6 5 6-5" stroke="#f6b21b" fill="none"/></svg><span>contact@kestran.example</span></div>
    <div class="ci-line" style="top:271px"></div>
    <div class="brand ci-brand"><span class="brand-mark"></span><span class="brand-name">KESTRAN</span></div>
  </div>
</section>

</div>
</body>
</html>
```